Quillspan

We need a 1 page flyer to showcase our public access phonebooth.
Meadowgate Outreach and Care Services
Connecting ones in need with loved ones
Flyer to indicate wired or wireless options.
The phone is VOIP based
LED lighting
Wireless option includes solar generation, and battery supply
Pictures need to be touched up to show warm summertime atmosphere
Ferncrest Color Pallette to be followed
www.ferncrestvoltix.com
email sales@ferncrestvoltix.com
Phone 780.555.0193

```html
<!DOCTYPE html>
<html lang="en">
<head>
<meta charset="utf-8">
<title>Quillspan Phone Booth Flyer</title>
<link rel="stylesheet" href="https://fonts.googleapis.com/css2?family=Montserrat:wght@500;600;700;800&display=swap">
<style>
  :root {
    --page-bg: #f1f1f1;
    --paper: #ffffff;
    --ink: #1d1d1f;
    --brand-blue: #3a4fa0;
    --sky-cyan: #4cc5ee;
    --leaf-green: #6cbf3c;
    --band-dark: #333333;
    --white: #ffffff;
  }
  * { box-sizing: border-box; margin: 0; padding: 0; }
  html, body { width: 800px; height: 1200px; overflow: hidden; }
  body {
    background: var(--page-bg);
    font-family: "Montserrat", Arial, sans-serif;
    position: relative;
  }
  .flyer {
    position: absolute; left: 0; top: 82px;
    width: 800px; height: 1035px;
    background: var(--paper);
    overflow: hidden;
    box-shadow: 0 6px 24px rgba(0,0,0,.12);
  }
  .hero-photo {
    position: absolute; left: 0; top: 0; width: 800px; height: 575px;
    background: linear-gradient(180deg, #cfcfcc 0%, #a49a8c 35%, #6f6555 60%, #56552f 82%, #403a2b 100%);
  }
  .headline {
    position: absolute; left: 41px; top: 370px;
    color: var(--white); font-weight: 800; text-transform: uppercase;
    line-height: 1;
  }
  .headline .line { display: block; font-size: 46px; letter-spacing: .5px; margin-bottom: 4px; }
  .headline .accent { color: var(--leaf-green); font-size: 34px; margin-top: 2px; }
  .tagline {
    position: absolute; left: 40px; top: 541px; width: 401px; height: 57px;
    background: var(--sky-cyan); color: var(--white);
    font-weight: 800; font-size: 20px; line-height: 24px;
    padding: 5px 0 0 17px; text-transform: uppercase;
  }
  .features { position: absolute; left: 40px; top: 620px; list-style: none; }
  .feature {
    display: flex; align-items: center; gap: 22px;
    font-size: 24px; font-weight: 700; color: var(--ink);
    line-height: 1.2; margin-bottom: 21px; min-height: 48px;
  }
  .feature-icon {
    flex: 0 0 48px; width: 48px; height: 48px; border-radius: 50%;
    background: var(--white); box-shadow: 0 1px 4px rgba(0,0,0,.22);
    display: flex; align-items: center; justify-content: center;
  }
  .frame-accent { position: absolute; background: var(--leaf-green); }
  .frame-accent.top-right { left: 617px; top: 538px; width: 142px; height: 138px; }
  .frame-accent.bottom-left { left: 505px; top: 731px; width: 144px; height: 142px; }
  .booth-photo {
    position: absolute; left: 521px; top: 553px; width: 225px; height: 301px;
    border: 4px solid var(--white);
    background: linear-gradient(160deg, #8a93ab 0%, #b9bcc0 50%, #d6d8da 100%);
    box-shadow: 0 2px 8px rgba(0,0,0,.2);
  }
  .brand {
    position: absolute; left: 48px; top: 978px;
    display: flex; align-items: center; gap: 8px;
    color: var(--brand-blue); font-weight: 700; font-size: 22px;
  }
  .brand-dot { width: 14px; height: 14px; border-radius: 50%; background: var(--sky-cyan); }
  .contact-band { position: absolute; left: 190px; top: 922px; width: 610px; height: 113px; }
  .contact-band .band-shape { position: absolute; left: 0; top: 0; }
  .call {
    position: absolute; left: 64px; top: 16px;
    font-size: 36px; font-weight: 700; color: var(--leaf-green); white-space: nowrap;
  }
  .call .number { color: var(--white); font-weight: 800; margin-left: 6px; }
  .contact-line {
    position: absolute; left: 64px; top: 70px;
    display: flex; gap: 16px; align-items: center;
    color: var(--white); font-size: 14px; font-weight: 600; white-space: nowrap;
  }
  .contact-item { display: flex; align-items: center; gap: 7px; }
  .contact-item svg { flex: 0 0 auto; display: block; }
</style>
</head>
<body>
  <main class="flyer">
    <div class="hero-photo" role="img" aria-label="Photo of a public phone booth on a grassy lot beside trees and a low building"></div>

    <h1 class="headline">
      <span class="line">Meadowgate</span>
      <span class="line">Outreach and</span>
      <span class="line accent">Care Services</span>
    </h1>

    <p class="tagline">Connecting ones in need<br>with loved ones</p>

    <ul class="features">
      <li class="feature">
        <span class="feature-icon">
          <svg width="26" height="26" viewBox="0 0 26 26" fill="none" stroke="var(--brand-blue)" stroke-width="1.6"><rect x="3" y="3" width="8" height="20" rx="2"/><rect x="11" y="6" width="12" height="17" rx="2"/><rect x="14" y="9" width="6" height="3"/><path d="M14 15h2M18 15h2M14 19h2M18 19h2"/></svg>
        </span>
        The phone is VOIP based
      </li>
      <li class="feature">
        <span class="feature-icon">
          <svg width="26" height="26" viewBox="0 0 26 26" fill="none" stroke="var(--brand-blue)" stroke-width="1.6"><circle cx="13" cy="11" r="6"/><path d="M10 17v3h6v-3M11 22h4M13 1v2M4 4l1.5 1.5M22 4l-1.5 1.5M1 11h2M23 11h2"/></svg>
        </span>
        LED lighting
      </li>
      <li class="feature">
        <span class="feature-icon">
          <svg width="26" height="26" viewBox="0 0 26 26" fill="none" stroke="var(--brand-blue)" stroke-width="1.6"><path d="M4 8h15l3 13H5z"/><path d="M9 8l1 13M14 8l2 13M4.8 12.5h15.5M5.5 17h15.8"/><circle cx="21" cy="4" r="2"/></svg>
        </span>
        Wireless option includes<br>solar generation
      </li>
      <li class="feature">
        <span class="feature-icon">
          <svg width="26" height="26" viewBox="0 0 26 26" fill="none" stroke="var(--brand-blue)" stroke-width="1.6"><rect x="8" y="5" width="10" height="18" rx="1.5"/><path d="M11 3h4v2M13 9l-2 5h4l-2 5"/></svg>
        </span>
        Battery supply
      </li>
    </ul>

    <div class="frame-accent top-right"></div>
    <div class="frame-accent bottom-left"></div>
    <div class="booth-photo" role="img" aria-label="Photo looking into the open phone booth with a wall-mounted phone"></div>

    <div class="brand"><span class="brand-dot"></span>Ferncrest</div>

    <section class="contact-band">
      <svg class="band-shape" width="610" height="113" viewBox="0 0 610 113">
        <polygon points="36,0 610,0 610,113 6,113" fill="var(--band-dark)"/>
        <polygon points="28,0 40,0 12,113 0,113" fill="var(--leaf-green)"/>
      </svg>
      <p class="call">Call us Today!<span class="number">780.555.0193</span></p>
      <div class="contact-line">
        <span class="contact-item">
          <svg width="14" height="10" viewBox="0 0 14 10"><rect width="14" height="10" fill="var(--leaf-green)"/><path d="M0 0l7 6 7-6" fill="none" stroke="var(--band-dark)" stroke-width="1.2"/></svg>
          <span>sales@ferncrestvoltix.com</span>
        </span>
        <span class="contact-item">
          <svg width="11" height="11" viewBox="0 0 12 12" fill="none" stroke="var(--leaf-green)" stroke-width="1.3"><circle cx="6" cy="6" r="5"/><path d="M1 6h10M6 1c-2.5 3-2.5 7 0 10M6 1c2.5 3 2.5 7 0 10"/></svg>
          <span>www.ferncrestvoltix.com</span>
        </span>
      </div>
    </section>
  </main>
</body>
</html>
```